Poster for our end of year annual dance concert

We need an A3 portrait poster for our end of year concert.
Designs are attached of posters from previous 3 years as a reference only.
The theme of our concert this year is "Comets & Lanterns ".
This is a fun them with dance routines choreographed to songs such as "Glimmerlass", "Fox Maiden", "Zip Lassie", "Quillor", "The Tinker", "Velvet Otters", "Drifters", "Gremlets", etc, etc
Dance styles in the concert include Jazz & Hip Hop.
Bright colors are preferred in the design.

Target Market(s)

Dance school students & their families

Industry/Entity Type

Dance Studio

Font styles to use
Sans Serif

Requirements
Must have
• Size: A3 Portrait
• You will see in the samples from previous years the poster must have:
• The Rosalind Pike Dancers (font is Mistral) + logo (supplied)
• Bellward Theatre
• Marlowe College Fernbrook
• Concert date this year is: Saturday 19th November
• Website: www.rpkdancers-site.com.au
Nice to have
• Clean design, not cluttered with too much imagery

```html
<!DOCTYPE html>
<html lang="en">
<head>
<meta charset="utf-8">
<title>Comets &amp; Lanterns – The Rosalind Pike Dancers</title>
<link rel="stylesheet" href="https://fonts.googleapis.com/css2?family=Dancing+Script:wght@600&family=Josefin+Sans:wght@300;400;600&display=swap">
<style>
  :root {
    --plum-top: #6e1f4a;
    --rose: #a3426c;
    --rose-soft: #b8587f;
    --night: #2b1b4a;
    --night-deep: #1a1133;
    --violet-glow: #6a3d8f;
    --accent: #d8437f;
    --white: #ffffff;
  }
  * { box-sizing: border-box; margin: 0; padding: 0; }
  html, body { width: 848px; height: 1200px; overflow: hidden; background: var(--night-deep); }
  .poster {
    position: relative;
    width: 848px;
    height: 1200px;
    overflow: hidden;
    font-family: "Josefin Sans", sans-serif;
    color: var(--white);
    background:
      radial-gradient(ellipse 60% 25% at 20% 78%, rgba(138, 70, 150, .55), transparent 70%),
      radial-gradient(ellipse 50% 20% at 85% 92%, rgba(170, 60, 130, .45), transparent 70%),
      linear-gradient(180deg, var(--plum-top) 0%, var(--rose) 30%, var(--rose-soft) 44%, var(--violet-glow) 52%, var(--night) 68%, var(--night-deep) 100%);
  }
  .hero-figure {
    position: absolute;
    left: 24px;
    top: 150px;
    width: 700px;
    height: 820px;
    border-radius: 46% 50% 40% 44%;
    background: radial-gradient(ellipse at 50% 45%, rgba(46, 37, 80, .95) 0%, rgba(46, 37, 80, .75) 45%, rgba(46, 37, 80, 0) 72%);
  }
  .studio-name {
    position: absolute;
    top: 22px;
    width: 100%;
    text-align: center;
    font-family: "Dancing Script", cursive;
    font-weight: 600;
    font-size: 44px;
    line-height: 60px;
    text-shadow: 0 2px 6px rgba(0, 0, 0, .45);
  }
  .presents {
    position: absolute;
    top: 112px;
    width: 100%;
    text-align: center;
    font-weight: 300;
    font-size: 22px;
    letter-spacing: 6px;
  }
  .show-title {
    position: absolute;
    inset: 0;
    font-weight: 400;
    text-transform: uppercase;
    line-height: 1;
    text-shadow: 0 3px 10px rgba(0, 0, 0, .35);
  }
  .title-first {
    position: absolute;
    left: 2px;
    top: 478px;
    font-size: 80px;
    letter-spacing: 4px;
    white-space: nowrap;
  }
  .title-first .initial { font-size: 142px; }
  .title-amp {
    position: absolute;
    left: 512px;
    top: 552px;
    font-size: 50px;
    color: var(--accent);
    text-shadow: none;
  }
  .title-second {
    position: absolute;
    left: 298px;
    top: 598px;
    font-size: 60px;
    letter-spacing: 12px;
    white-space: nowrap;
  }
  .title-second .initial { font-size: 118px; letter-spacing: 4px; }
  .event-box {
    position: absolute;
    left: 62px;
    top: 900px;
    width: 724px;
    height: 168px;
    padding-top: 26px;
    border: 1.5px solid rgba(255, 255, 255, .9);
    text-align: center;
    text-transform: uppercase;
    box-shadow: 0 0 10px rgba(255, 255, 255, .15);
  }
  .event-date {
    font-weight: 400;
    font-size: 40px;
    line-height: 44px;
    letter-spacing: 1.5px;
  }
  .event-venue {
    font-weight: 300;
    font-size: 32px;
    line-height: 42px;
    letter-spacing: 1px;
  }
  .website {
    position: absolute;
    top: 1148px;
    width: 100%;
    text-align: center;
    font-weight: 400;
    font-size: 17px;
    letter-spacing: 9px;
  }
  .studio-mark {
    position: absolute;
    right: 16px;
    bottom: 14px;
    display: flex;
    align-items: center;
    gap: 6px;
    font-weight: 600;
    font-size: 18px;
  }
  .studio-mark .square {
    width: 14px;
    height: 14px;
    background: var(--accent);
  }
</style>
</head>
<body>
  <main class="poster">
    <div class="hero-figure" role="img" aria-label="Silhouette of a leaping dancer with arms outstretched against a starry night sky"></div>

    <h2 class="studio-name">The Rosalind Pike Dancers</h2>
    <p class="presents">presents</p>

    <h1 class="show-title">
      <span class="title-first"><span class="initial">C</span>omets</span>
      <span class="title-amp">&amp;</span>
      <span class="title-second"><span class="initial">L</span>anterns</span>
    </h1>

    <section class="event-box">
      <p class="event-date">Saturday 19th November</p>
      <p class="event-venue">Bellward Theatre</p>
      <p class="event-venue">Marlowe College Fernbrook</p>
    </section>

    <p class="website">www.rpkdancers-site.com.au</p>

    <div class="studio-mark"><span class="square"></span>RPD</div>
  </main>
</body>
</html>
```